TK Joinery

Cabinet maker. Kitchens. Wardrobes. Vanitys. Entertainment units

Target Market(s)

Modern contemporary.geometry. colours black, gray, charcoal and orange. Matt card gloss letters

Industry/Entity Type

Entertainment

Contact Information for Business Card

Marcel Otvany 0417 382 594
marcel.otvany@fernmail.test
ABN 731 4928 5170

Font styles to use
Decorative

Colors
000000

Requirements
Should not have
• Pictures

```html
<!DOCTYPE html>
<html lang="en">
<head>
<meta charset="utf-8">
<title>TK Joinery – Business Card</title>
<link rel="stylesheet" href="https://fonts.googleapis.com/css2?family=Open+Sans:wght@400;600;700&display=swap">
<style>
  :root {
    --backdrop: #e9e7e4;
    --card-charcoal: #2b2b2b;
    --card-orange: #ff5a00;
    --mark-on-charcoal: #4a4a4a;
    --mark-on-orange: #c94400;
    --text-light: #ffffff;
  }
  * { box-sizing: border-box; margin: 0; padding: 0; }
  html, body {
    width: 1200px;
    height: 900px;
    overflow: hidden;
    background: var(--backdrop);
    font-family: "Open Sans", Arial, sans-serif;
  }
  .canvas {
    position: relative;
    width: 1200px;
    height: 900px;
  }
  .card {
    position: absolute;
    box-shadow: 0 4px 14px rgba(0, 0, 0, 0.18);
  }
  .card--front {
    left: 238px;
    top: 62px;
    width: 556px;
    height: 342px;
    background: var(--card-charcoal);
  }
  .card--back {
    left: 457px;
    top: 518px;
    width: 560px;
    height: 343px;
    background: var(--card-orange);
  }
  .brand-mark {
    position: absolute;
    font-weight: 700;
    white-space: nowrap;
    line-height: 1;
  }
  .card--front .brand-mark {
    left: 56px;
    top: 232px;
    font-size: 46px;
    color: var(--mark-on-charcoal);
  }
  .card--back .brand-mark {
    left: 0;
    right: 0;
    top: 142px;
    text-align: center;
    font-size: 56px;
    color: var(--mark-on-orange);
    letter-spacing: 1px;
  }
  .holder-name {
    position: absolute;
    right: 38px;
    top: 96px;
    color: var(--text-light);
    font-size: 20px;
    font-weight: 600;
  }
  .contact-list {
    position: absolute;
    right: 38px;
    top: 187px;
    list-style: none;
    color: var(--text-light);
    font-size: 14.5px;
    line-height: 21px;
    text-align: right;
  }
  .contact-list li {
    display: flex;
    align-items: center;
    justify-content: flex-end;
    gap: 9px;
  }
  .contact-icon {
    width: 11px;
    height: 11px;
    fill: var(--text-light);
    flex: none;
  }
  .contact-spacer {
    width: 11px;
    flex: none;
  }
</style>
</head>
<body>
<main class="canvas">
  <section class="card card--front" aria-label="Business card front">
    <span class="brand-mark">TK Joinery</span>
    <h1 class="holder-name">Marcel Otvany</h1>
    <ul class="contact-list">
      <li>0417 382 594
        <svg class="contact-icon" viewBox="0 0 24 24" aria-hidden="true"><path d="M6.6 10.8a15.1 15.1 0 0 0 6.6 6.6l2.2-2.2a1 1 0 0 1 1-.25 11.4 11.4 0 0 0 3.6.57 1 1 0 0 1 1 1V20a1 1 0 0 1-1 1A17 17 0 0 1 3 4a1 1 0 0 1 1-1h3.5a1 1 0 0 1 1 1c0 1.25.2 2.45.57 3.570a1 1 0 0 1-.25 1z"/></svg>
      </li>
      <li>marcel.otvany@fernmail.test
        <svg class="contact-icon" viewBox="0 0 24 24" aria-hidden="true"><path d="M2 6v13h20V6l-10 7.5z"/><path d="M2.8 5h18.4L12 11.8z"/></svg>
      </li>
      <li>ABN 731 4928 5170
        <span class="contact-spacer" aria-hidden="true"></span>
      </li>
    </ul>
  </section>

  <section class="card card--back" aria-label="Business card back">
    <span class="brand-mark">TK Joinery</span>
  </section>
</main>
</body>
</html>
```